We need a package design for a dietary supplement.

We need a package design for a dietary supplement - throwable tablets - Senegalese acacia fiber with pineapple flavor.
New name BrioKern.
Remember the packaging is a white jar, a magenta cap, a sticker, and a cardboard box. We want to change the name to: BrioKern (if you have a better idea for the name, just tell me) and refresh the packaging.
Product description:
> Contributes to improving the functioning of the digestive system.
> Boosts metabolism, controls appetite and supports weight loss.
> Helps maintain normal blood sugar levels.
> Regulates cholesterol levels
> 100% natural ingredients in the form of chewable tablets.
It has many beneficial health benefits:
> Cleanses the body of toxins,
> Helps with constipation and bloating,
> Facilitates defecation,
> Regulates cholesterol levels (by eliminating bile acids from the intestine),
> Adds energy,
> Improves metabolism,
> reduces appetite,
> Improves the work of the digestive system,
> It can help to get rid of the unpleasant smell from the mouth,
> Improves well-being,
> Regular intake can lead to weight loss,
> It works gently and does not cause side effects,
> Delays the aging process,
> Improves the appearance of the skin
This all-natural dietary supplement supports heart health, helps maintain blood sugar levels, soothes irritable bowel syndrome, and improves overall gut health.

100% natural, vegan product, no added sugars, no added salt. It has only 2 ingredients: Cenegal acacia and pineapple juice.

We are changing the name and packaging for our product called DunaMarsk. Photos attached, packaging grid attached, samples of our other packaging attached.
*Packaging in Dutch

Target Market(s)

Netherlands

Industry/Entity Type

dietary supplements

Colors

Designer to choose colors to be used in the design.

Requirements
Must have
• Modern and inspire patient confidence.
Nice to have
• Good, natural, healthy
Should not have
• It should not clearly indicate that it has a slimming effect, as in the dunamarsk project

```html
<!DOCTYPE html>
<html lang="nl">
<head>
<meta charset="utf-8">
<title>BrioKern – Etiket pot</title>
<link href="https://fonts.googleapis.com/css2?family=Montserrat:wght@500;700;800&family=Nunito:wght@400;600&display=swap" rel="stylesheet">
<style>
  :root {
    --magenta: #d4097a;
    --navy: #1a2a52;
    --label-white: #f4f4f4;
    --page: #ffffff;
  }
  * { margin: 0; padding: 0; box-sizing: border-box; }
  html, body {
    width: 1200px; height: 1200px; overflow: hidden;
    background: var(--page);
  }
  .label {
    position: absolute; left: 130px; top: 75px;
    width: 940px; height: 1050px;
    background: linear-gradient(90deg, #efefef 0%, var(--label-white) 40%, #f7f7f7 100%);
    overflow: hidden;
    font-family: "Nunito", sans-serif;
  }
  .side-panel { position: absolute; inset: 0; width: 940px; height: 1050px; }
  .brand {
    position: absolute; left: 105px; top: 118px;
    font-family: "Montserrat", sans-serif; font-weight: 800;
    font-size: 52px; letter-spacing: -1px; color: var(--navy);
    display: flex; align-items: center; gap: 12px;
  }
  .brand-dot { width: 16px; height: 16px; border-radius: 50%; background: var(--magenta); }
  .product-name {
    position: absolute; left: 70px; top: 255px;
    font-family: "Montserrat", sans-serif; font-weight: 800;
    font-size: 150px; line-height: 1; letter-spacing: -4px;
  }
  .product-name .first { color: var(--magenta); }
  .product-name .second { color: var(--navy); }
  .ingredient-pill {
    position: absolute; left: 73px; top: 438px;
    height: 52px; border-radius: 26px;
    background: var(--magenta); color: #fff;
    font-family: "Montserrat", sans-serif; font-weight: 500;
    font-size: 27px; letter-spacing: 3px;
    display: flex; align-items: center; padding: 0 28px 0 22px;
  }
  .benefits { position: absolute; left: 108px; top: 560px; list-style: none; }
  .benefits li {
    display: flex; align-items: center; gap: 12px;
    font-size: 36px; color: var(--navy); height: 54px;
    text-transform: uppercase; letter-spacing: -0.5px;
    white-space: nowrap;
  }
  .benefits svg { width: 34px; height: 38px; flex: none; }
  .badge {
    position: absolute; top: 750px; width: 180px; text-align: center;
    font-family: "Montserrat", sans-serif; font-weight: 500;
    font-size: 14px; line-height: 1.3; letter-spacing: 1px; color: var(--navy);
  }
  .badge svg { width: 86px; height: 86px; display: block; margin: 0 auto 10px; }
  .badge--sugar { left: 110px; }
  .badge--vegan { left: 300px; }
  .count-box {
    position: absolute; left: 84px; top: 917px;
    width: 152px; height: 133px; background: var(--magenta);
    border-radius: 10px 10px 0 0; color: #fff; text-align: center;
    padding-top: 14px;
  }
  .count-box .num { font-family: "Montserrat", sans-serif; font-weight: 800; font-size: 64px; line-height: 1; letter-spacing: -2px; }
  .count-box .unit { font-size: 27px; text-transform: uppercase; }
  .ingredient-visual {
    position: absolute; left: 540px; top: 740px;
    width: 400px; height: 310px;
    border-radius: 55% 0 0 30% / 60% 0 0 40%;
    background: radial-gradient(ellipse at 75% 30%, #f6d33a 0%, #f0b322 35%, #c8743a 68%, #9b4a2a 100%);
  }
</style>
</head>
<body>
  <div class="label">
    <svg class="side-panel" viewBox="0 0 940 1050" aria-hidden="true">
      <defs>
        <linearGradient id="panelGrad" x1="0" x2="1" y1="0" y2="0">
          <stop offset="0" stop-color="#f2f2f2"/>
          <stop offset="0.45" stop-color="#d4d4d4"/>
          <stop offset="1" stop-color="#a8a8a8"/>
        </linearGradient>
      </defs>
      <path d="M768 0 H940 V1050 H620 C760 760 850 420 768 0 Z" fill="url(#panelGrad)"/>
      <path d="M748 0 C840 330 810 700 592 1050" fill="none" stroke="var(--magenta)" stroke-width="9"/>
    </svg>

    <div class="brand"><span>Nordavel</span><span class="brand-dot"></span></div>

    <h1 class="product-name"><span class="first">BRIO</span><span class="second">KERN</span></h1>
    <div class="ingredient-pill">SENEGALESE ACACIAVEZEL</div>

    <ul class="benefits">
      <li><svg viewBox="0 0 34 38"><path d="M3 21 L13 33 L31 3" fill="none" stroke="var(--navy)" stroke-width="5" stroke-linecap="round" stroke-linejoin="round"/></svg>Reguleert cholesterol</li>
      <li><svg viewBox="0 0 34 38"><path d="M3 21 L13 33 L31 3" fill="none" stroke="var(--navy)" stroke-width="5" stroke-linecap="round" stroke-linejoin="round"/></svg>Stimuleert stofwisseling</li>
      <li><svg viewBox="0 0 34 38"><path d="M3 21 L13 33 L31 3" fill="none" stroke="var(--navy)" stroke-width="5" stroke-linecap="round" stroke-linejoin="round"/></svg>Vermindert eetlust</li>
    </ul>

    <div class="badge badge--sugar">
      <svg viewBox="0 0 86 86" aria-hidden="true">
        <circle cx="43" cy="43" r="39" fill="none" stroke="var(--magenta)" stroke-width="3"/>
        <rect x="26" y="30" width="20" height="20" fill="var(--magenta)"/>
        <rect x="42" y="36" width="20" height="20" fill="var(--magenta)" opacity="0.8"/>
        <line x1="18" y1="18" x2="68" y2="68" stroke="var(--magenta)" stroke-width="3"/>
      </svg>
      ZONDER TOEGEVOEGD<br>SUIKER OF ZOUT
    </div>
    <div class="badge badge--vegan">
      <svg viewBox="0 0 86 86" aria-hidden="true">
        <circle cx="43" cy="43" r="39" fill="none" stroke="var(--magenta)" stroke-width="3"/>
        <path d="M43 60 C28 58 22 46 24 32 C36 34 43 44 43 60 Z" fill="var(--magenta)"/>
        <path d="M43 60 C58 58 64 46 62 32 C50 34 43 44 43 60 Z" fill="var(--magenta)"/>
      </svg>
      VEGANISTISCH<br>PRODUCT
    </div>

    <div class="count-box"><div class="num">100</div><div class="unit">Capsules</div></div>

    <div class="ingredient-visual" role="img" aria-label="Ananasstukken met brokjes amberkleurige acaciagom"></div>
  </div>
</body>
</html>
```